Webdesign für Finanzberatung
Sehr schönes Design. Auf Änderungswünsche wurde sehr schnell reagiert. Bin sehr zufrieden!
Zielgruppe
Ganzheitliche Finanzberatung / Finanzcoaching (Geldanlage, Investment, ETFs, Fonds, Aktien) für eine digital affine Zielgruppe. Es handelt sich um eine Beratung / um ein Coaching gegen Honorar.
Aufgabenstellung
Die Webseite sollte die Elemente 'digital' (Roboter) und 'persönlich' (Mensch) kombinieren. Das Design sollte modern sein und eine digital affine Zielgruppe ansprechen. Gleichzeitig soll das Thema 'persönliche Finanzberatung' zum Ausdruck gebracht werden.

```html
<!DOCTYPE html>
<html lang="de">
<head>
<meta charset="utf-8">
<title>Finanzhafen – Finanzberatung</title>
<link href="https://fonts.googleapis.com/css2?family=Open+Sans:ital,wght@0,400;0,600;0,700;1,400;1,600&family=Barlow:wght@600;700&display=swap" rel="stylesheet">
<style>
:root{
  --stage:#6b6b6b;
  --page:#ffffff;
  --ink:#111418;
  --grey-text:#555a60;
  --blue:#2e6aa3;
  --card-side:#7a9aba;
  --card-main:#416f9c;
  --btn-dark:#37434f;
  --hero-a:#bcdcf3;
  --hero-b:#7fb8de;
  --band:rgba(95,185,205,.55);
  --teal:#33a6ae;
  --footer:#0a0a0c;
  --field:#d8dbe0;
}
*{margin:0;padding:0;box-sizing:border-box}
html,body{width:1200px;height:2400px;overflow:hidden;background:var(--stage);font-family:"Open Sans",Arial,sans-serif;color:var(--ink)}
.page{position:absolute;left:300px;top:20px;width:600px;height:2360px;background:var(--page);overflow:hidden}
.abs{position:absolute}
.center{text-align:center}

/* header */
.brand{left:14px;top:12px;display:flex;align-items:center;gap:6px}
.brand-dot{width:14px;height:14px;border:2px solid var(--blue);border-radius:50%}
.brand-name{font-size:13px;font-weight:600;color:var(--blue);letter-spacing:1.5px}
.nav{right:9px;top:40px;display:flex;gap:13px;font-size:8.5px;color:var(--blue)}
.nav .active{color:var(--ink)}

/* hero */
.hero{left:0;top:53px;width:600px;height:326px;background:linear-gradient(160deg,var(--hero-a) 0%,#9fcbec 45%,var(--hero-b) 100%)}
.hero-band{left:0;top:270px;width:600px;height:109px;background:var(--band)}
.hero-title{left:0;width:600px;font-family:"Barlow",sans-serif;font-weight:700;font-size:25px;letter-spacing:2px;color:var(--ink);line-height:32px}
.hero-cta{left:0;top:344px;width:600px;font-size:14px;font-weight:600;color:#fff;letter-spacing:1px}

/* intro */
.h2{font-size:17.5px;font-weight:600;letter-spacing:1.5px}
.lead{font-size:11.5px;line-height:12.6px;letter-spacing:.4px}
.icon{width:42px;height:42px}
.col-text{width:182px;font-size:8.3px;line-height:12.6px;letter-spacing:.3px}

/* cards */
.card{border-radius:7px;color:#fff;box-shadow:0 1px 3px rgba(0,0,0,.15)}
.card-side{background:var(--card-side);width:212px;height:260px}
.card-main{background:var(--card-main);width:212px;height:259px}
.card-title{position:absolute;left:20px;top:24px;width:180px;font-size:11px;font-weight:700;line-height:12.5px;letter-spacing:.4px;white-space:nowrap}
.card-text{position:absolute;left:21px;top:62px;width:170px;font-size:8px;line-height:10px}
.card-price{position:absolute;left:21px;top:116px;font-size:13px;font-weight:700}
.card-price small{font-size:6px;font-style:italic;font-weight:400}
.card-btn{position:absolute;left:35px;top:172px;width:154px;height:34px;background:var(--btn-dark);border-radius:4px;font-size:14px;font-style:italic;letter-spacing:1px;display:flex;align-items:center;justify-content:center}

/* about */
.about-h{left:86px;top:1248px;font-size:17px;font-weight:600;letter-spacing:1.5px;color:var(--grey-text)}
.about-p{left:88px;top:1275px;width:420px;font-size:11.2px;line-height:12.5px;letter-spacing:.5px;color:var(--grey-text)}
.feat-h{left:92px;font-size:12px;font-weight:700;color:var(--blue)}
.feat-p{left:93px;width:210px;font-size:8.8px;line-height:10.5px;color:#777c82}
.portrait{left:307px;top:1500px;width:206px;height:164px;background:radial-gradient(ellipse at 50% 40%,#e9d6c6 0%,#c7d8e8 55%,#ffffff 100%)}
.rule{left:92px;top:1664px;width:421px;height:1px;background:#8a9097}
.cta-btn{left:212px;top:1676px;width:203px;height:34px;background:var(--btn-dark);border-radius:5px;color:#fff;font-size:11px;font-style:italic;font-weight:600;letter-spacing:.8px;display:flex;align-items:center;justify-content:center}

/* testimonials */
.testimonials{left:0;top:1786px;width:600px;height:248px;background:var(--teal)}
.kicker{font-size:5.5px;font-weight:700;letter-spacing:.3px}
.t-head{font-family:"Barlow",sans-serif;font-size:17px;font-weight:700;letter-spacing:.3px}
.t-sub{font-size:8.5px;line-height:10.5px}
.quote{width:110px;font-size:8px;line-height:10px}
.quote b{display:block;font-size:6.5px;font-weight:700}
.quote i{display:block;font-size:6.5px;margin-bottom:6px}

/* contact */
.c-head{left:88px;font-family:"Barlow",sans-serif;font-weight:700;font-size:11px;letter-spacing:.3px}
.c-line{left:88px;font-size:11px;color:#a8adb3;display:flex;align-items:center;gap:6px}
.socials{left:88px;top:2206px;display:flex;gap:12px}
.socials span{width:14px;height:14px;border:1.5px solid #a8adb3;border-radius:50%}
.q-kicker{left:367px;top:2066px;font-size:5px;font-weight:700}
.q-head{left:367px;top:2076px;font-family:"Barlow",sans-serif;font-weight:700;font-size:12px}
.q-sub{left:369px;top:2092px;font-size:8px;font-weight:600}
.field{border:1px solid var(--field);border-radius:6px;font-size:5px;color:#777;padding:3px 6px}
.send{left:376px;top:2237px;width:65px;height:12px;background:#6f7378;border-radius:6px;color:#fff;font-size:7px;letter-spacing:.8px;display:flex;align-items:center;justify-content:center}

/* footer */
.footer{left:0;top:2295px;width:600px;height:65px;background:var(--footer);color:#b8bcc2}
.footer-left{position:absolute;left:26px;top:39px;font-size:7.5px}
.footer-right{position:absolute;right:25px;top:41px;font-size:5px}
</style>
</head>
<body>
<main class="page">

  <header>
    <div class="abs brand"><span class="brand-dot"></span><span class="brand-name">FINANZHAFEN</span></div>
    <nav class="abs nav"><span class="active">Home</span><span>Leistungen</span><span>Über mich</span><span>Kontakt</span></nav>
  </header>

  <section>
    <div class="abs hero" role="img" aria-label="Foto: Roboterhand und menschliche Hand berühren einen Bildschirm mit digitalem Netzwerk"></div>
    <div class="abs hero-band"></div>
    <h1 class="abs hero-title center" style="top:280px">FINANZENTSCHEIDUNGEN PERSONALISIEREN<br>FINANZEN DIGITALISIEREN</h1>
    <div class="abs hero-cta center">Erstberatung buchen &gt;&gt;</div>
  </section>

  <section>
    <h2 class="abs h2 center" style="left:0;width:600px;top:424px">LOREM IPSUM IPOSUM DOLOR</h2>
    <p class="abs lead center" style="left:92px;width:444px;top:455px">Cum sociis natoque penatibus et magnis dis parturient montes, nascetur ridiculus mus. Donec quam felis, ultricies nec, pellentesque eu, pretium quis, sem. Nulla consequat massa quis enim. Donec pede justo, fringilla vel, aliquet nec, vulputate eget, arcu. In enim justo, rhoncus ut, imperdiet a, venenatis vitae, justo.</p>

    <svg class="abs icon" style="left:152px;top:537px" viewBox="0 0 42 42" fill="none" stroke="#3a78c9" stroke-width="1.4">
      <circle cx="21" cy="21" r="13"/>
      <circle cx="21" cy="21" r="7"/>
      <circle cx="21" cy="21" r="2.5"/>
      <path d="M21 4v4M21 34v4M4 21h4M34 21h4M9 9l3 3M30 30l3 3M9 33l3-3M30 12l3-3"/>
    </svg>
    <svg class="abs icon" style="left:427px;top:535px" viewBox="0 0 42 42" fill="none" stroke="#4b5bd0" stroke-width="1.4">
      <path d="M21 3a17 17 0 1 1-9 31.5L5 38l3-7A17 17 0 0 1 21 3z"/>
      <path d="M21 30V12M15 13v7l6 4M27 13v7l-6 4"/>
      <circle cx="21" cy="11" r="1.5"/><circle cx="15" cy="12" r="1.5"/><circle cx="27" cy="12" r="1.5"/>
    </svg>

    <p class="abs col-text" style="left:94px;top:587px">Cum sociis natoque penatibus et magnis dis parturient montes, nascetur ridiculus mus. Donec quam felis, ultricies nec, pellentesque eu, pretium quis, sem. Nulla consequat massa quis enim. Donec pede justo, fringilla vel, aliquet nec, vulputate eget, arcu. In enim justo, rhoncus ut, imperdiet a, venenatis vitae, justo.</p>
    <p class="abs col-text" style="left:351px;top:585px">Cum sociis natoque penatibus et magnis dis parturient montes, nascetur ridiculus mus. Donec quam felis, ultricies nec, pellentesque eu, pretium quis, sem. Nulla consequat massa quis enim. Donec pede justo, fringilla vel, aliquet nec, vulputate eget, arcu. In enim justo, rhoncus ut, imperdiet a, venenatis vitae, justo.</p>
  </section>

  <section>
    <h2 class="abs h2 center" style="left:0;width:600px;top:756px">MEINE LEISTUNGEN</h2>
    <p class="abs lead center" style="left:150px;width:330px;top:789px">Cum sociis natoque penatibus et magnis dis parturient montes, nascetur ridiculus mus.</p>

    <article class="abs card card-side" style="left:350px;top:875px">
      <div class="card-title">Persönliches Coaching und<br>Begleitung</div>
      <p class="card-text">Nullam dictum felis eu pede mollis pretium. Integer tincidunt. Cras dapibus. Vivamus elementum semper nisi. Aenean vulputate eleifend tellus.</p>
      <div class="card-price">€ 290,-- <small>(inkl. Mwst.)</small></div>
      <div class="card-btn">buchen</div>
    </article>
    <article class="abs card card-side" style="left:42px;top:879px">
      <div class="card-title">Das&nbsp; minimal funktionsfähige<br>Portfolio</div>
      <p class="card-text">Nullam dictum felis eu pede mollis pretium. Integer tincidunt. Cras dapibus. Vivamus elementum semper nisi. Aenean vulputate eleifend tellus.</p>
      <div class="card-price">€ 90,-- <small>(inkl. Mwst.)</small></div>
      <div class="card-btn">buchen</div>
    </article>
    <article class="abs card card-main" style="left:230px;top:899px">
      <div class="card-title">Finanzplan und Vermögens-<br>management</div>
      <p class="card-text">Nullam dictum felis eu pede mollis pretium. Integer tincidunt. Cras dapibus. Vivamus elementum semper nisi. Aenean vulputate eleifend tellus.</p>
      <div class="card-price">€ 190,-- <small>(inkl. Mwst.)</small></div>
      <div class="card-btn">buchen</div>
    </article>
  </section>

  <section>
    <h2 class="abs about-h">ÜBER MICH</h2>
    <p class="abs about-p">Phasellus viverra nulla ut metus varius laoreet. Quisque rutrum. Aenean imperdiet. Etiam ultricies nisi vel augue. Curabitur ullamcorper ultricies nisi. Nam eget dui. Etiam rhoncus. Maecenas tempus, tellus eget condimentum rhoncus, sem quam semper libero, sit amet adipiscing sem neque sed ipsum. Phasellus viverra nulla ut metus varius laoreet. Quisque rutrum. Aenean imperdiet. Etiam ultricies nisi vel augue. Curabitur ullamcorper ultricies nisi. Nam eget dui. Etiam rhoncus. Maecenas tempus, tellus eget condimentum rhoncus, sem quam semper libero, sit amet adipiscing sem neque sed ipsum.</p>

    <h3 class="abs feat-h" style="top:1423px">Beste Finanzplanung</h3>
    <p class="abs feat-p" style="top:1441px">Lorem ipsum dolor sit amet, consectetur adipiscing elit, sed do eiusmod tempor incididunt ut labore et dolore magna aliqua.</p>
    <h3 class="abs feat-h" style="top:1503px">Expertenwissen</h3>
    <p class="abs feat-p" style="top:1520px">Lorem ipsum dolor sit amet, consectetur adipiscing elit, sed do eiusmod tempor incididunt ut labore et dolore magna aliqua.</p>
    <h3 class="abs feat-h" style="top:1591px">Persönliches Coaching</h3>
    <p class="abs feat-p" style="top:1609px">Lorem ipsum dolor sit amet, consectetur adipiscing elit, sed do eiusmod tempor incididunt ut labore et dolore magna aliqua.</p>

    <div class="abs portrait" role="img" aria-label="Porträtfoto des Finanzberaters"></div>
    <div class="abs rule"></div>
    <div class="abs cta-btn">Erstberatung buchen</div>
  </section>

  <section class="abs testimonials">
    <div class="abs kicker center" style="left:0;width:600px;top:38px">TESTIMONIALS</div>
    <h2 class="abs t-head center" style="left:0;width:600px;top:50px">WAS UNSERE KUNDEN SAGEN</h2>
    <p class="abs t-sub center" style="left:0;width:600px;top:71px">Lorem ipsum dolor sit amet, consectetur<br>adipiscing elit, sed do eiusmod tempor incididunt</p>
    <div class="abs quote center" style="left:128px;top:119px"><b>JONAS BERGER</b><i>CEO</i>“ Vestibulum sollicitudin nunc in eros a justo facilisis rutrum. Aenean id ullamcorper libero. Vestibulum imperdiet</div>
    <div class="abs quote center" style="left:257px;top:118px"><b>DANIEL REITER</b><i>Manager</i>“ Sollicitudin nunc in eros a justo facilisis rutrum. Aenean id ullamcorper libero. Vestibulum imperdiet nibh tortor mauris condimentum</div>
    <div class="abs quote center" style="left:391px;top:118px"><b>MARIE POHL</b><i>Angestellte</i>“ Sollicitudin nunc in eros a justo facilisis rutrum. Aenean id ullamcorper libero. Vestibulum imperdiet nibh tortor</div>
  </section>

  <section>
    <h3 class="abs c-head" style="top:2075px">GET IN TOUCH</h3>
    <div class="abs c-line" style="top:2101px">
      <svg width="14" height="10" viewBox="0 0 14 10" fill="none" stroke="#a8adb3"><rect x=".5" y=".5" width="13" height="9"/><path d="M.5 .5L7 6l6.5-5.5"/></svg>info@finanzhafen.de</div>
    <div class="abs c-line" style="top:2130px">
      <svg width="13" height="13" viewBox="0 0 13 13" fill="none" stroke="#a8adb3"><path d="M3 1l2 3-1.5 1.5a7 7 0 0 0 4 4L9 8l3 2-1 2.5C6 12 1 7 .8 2z"/></svg>040 / 55512390</div>
    <h3 class="abs c-head" style="top:2181px">FOLLOW US</h3>
    <div class="abs socials"><span></span><span></span><span></span></div>

    <div class="abs q-kicker">GET A QUOTE</div>
    <h3 class="abs q-head">Hinterlassen Sie eine Nachricht</h3>
    <div class="abs q-sub">Lorem ipsum dolor</div>
    <div class="abs field" style="left:367px;top:2116px;width:147px;height:12px">Name</div>
    <div class="abs field" style="left:367px;top:2136px;width:69px;height:12px">Telefonnummer</div>
    <div class="abs field" style="left:439px;top:2136px;width:69px;height:12px">Email</div>
    <div class="abs field" style="left:367px;top:2155px;width:148px;height:69px">Nachricht</div>
    <div class="abs send">SENDEN</div>
  </section>

  <footer class="abs footer">
    <div class="footer-left">IMPRESSUM I DATENSCHUTZ</div>
    <div class="footer-right">copyright Finanzhafen 2021</div>
  </footer>

</main>
</body>
</html>
```